Fontenot Bayou Grillhouse (Owners Card)

Need a classy, but modern business card. I have included a promotional card for the steakhouse. I need one for myself (the owner) that is more professional.

Target Market(s)

General Public

Industry/Entity Type

Food service

Contact Information for Business Card

Name, business address, phone number, email, logo

Font styles to use
Serif
Sans Serif
Decorative
Script

Requirements
Must have
• My name (Darvel Pruitt), business address (327 Oakmere Street), phone number (510) 493-2615, email (Dpruittkr4@mailvane.example. On the back of the card: Psalms 27 1 The LORD is my light and my salvation— whom shall I fear? The LORD is the stronghold of my life— of whom shall I be afraid? 2 When the wicked advance against me to devour me, it is my enemies and my foes who will stumble and fall. 3 Though an army besiege me, my heart will not fear; though war break out against me, even then I will be confident.
Nice to have
• Something that’s bold, but modern and professional.

```html
<!DOCTYPE html>
<html lang="en">
<head>
<meta charset="utf-8">
<title>Fontenot Bayou Grillhouse — Owner's Card</title>
<link rel="stylesheet" href="https://fonts.googleapis.com/css2?family=Lora:ital,wght@0,400;0,600;0,700;1,400&display=swap">
<style>
  :root {
    --stage: #2b2b2b;
    --card: #0f0f0f;
    --ink: #f2f2f2;
    --gold: #f0a81c;
    --green: #6cc04a;
    --yellow: #d9b12a;
    --orange: #ee8a22;
    --red: #e0262b;
    --brand: #ee6a24;
  }
  * { box-sizing: border-box; margin: 0; padding: 0; }
  html, body { width: 1200px; height: 900px; overflow: hidden; }
  body {
    background: var(--stage);
    font-family: "Lora", Georgia, serif;
    position: relative;
  }
  .card {
    position: absolute;
    left: 260px;
    width: 680px;
    height: 388px;
    background: var(--card);
    overflow: hidden;
    box-shadow: 0 10px 30px rgba(0,0,0,.55);
  }
  .card--back { top: 42px; }
  .card--front { top: 470px; }
  .card__band { position: absolute; left: 0; top: 0; width: 680px; height: 388px; }

  .verse {
    position: absolute;
    left: 44px;
    top: 46px;
    width: 430px;
    color: var(--ink);
    font-size: 14.5px;
    line-height: 1.45;
  }
  .verse p + p { margin-top: 12px; }
  .verse__ref { color: var(--gold); font-weight: 700; }

  .brand {
    position: absolute;
    display: flex;
    align-items: center;
    gap: 10px;
    color: var(--brand);
    font-weight: 700;
    font-size: 21px;
    line-height: 1.15;
  }
  .brand__dot {
    flex: none;
    width: 16px; height: 16px;
    border-radius: 50%;
    background: var(--brand);
  }
  .card--back .brand { left: 456px; top: 160px; width: 210px; }
  .card--front .brand { left: 456px; top: 90px; width: 210px; }

  .website {
    position: absolute;
    color: #1a0d06;
    font-weight: 700;
    font-size: 16px;
  }
  .card--back .website { left: 60px; top: 349px; }
  .card--front .website { right: 60px; top: 349px; }

  .owner {
    position: absolute;
    left: 80px;
    top: 150px;
  }
  .owner__name {
    font-size: 27px;
    font-weight: 700;
    letter-spacing: .5px;
    text-transform: uppercase;
    background: linear-gradient(90deg, var(--green), var(--yellow) 45%, var(--orange) 70%, var(--red));
    -webkit-background-clip: text;
    background-clip: text;
    color: transparent;
  }
  .contact { list-style: none; margin-top: 28px; }
  .contact__item {
    display: flex;
    align-items: center;
    gap: 12px;
    color: var(--ink);
    font-size: 17px;
    line-height: 1.7;
  }
  .contact__icon { width: 18px; height: 18px; flex: none; }
</style>
</head>
<body>

<section class="card card--back" aria-label="Card back">
  <svg class="card__band" viewBox="0 0 680 388" aria-hidden="true">
    <defs>
      <linearGradient id="band-back" x1="0" y1="0" x2="1" y2="0">
        <stop offset="0" stop-color="#e0262b"/>
        <stop offset=".35" stop-color="#ee8a22"/>
        <stop offset=".7" stop-color="#d9b12a"/>
        <stop offset="1" stop-color="#6cc04a"/>
      </linearGradient>
    </defs>
    <path d="M0 332 H300 Q318 332 327 346 L338 366 Q344 374 356 374 H680 V388 H0 Z" fill="url(#band-back)"/>
  </svg>

  <div class="verse">
    <p><span class="verse__ref">Psalms 27 1 The LORD</span> is my light and my salvation— whom shall I fear?<br>The LORD is the stronghold of my life— of whom shall I be afraid?</p>
    <p>When the wicked advance against me to devour me,<br>it is my enemies and my foes who will stumble and fall.</p>
    <p>Though an army besiege me, my heart will not fear;<br>though war break out against me, even then I will be confident.</p>
  </div>

  <div class="brand"><span class="brand__dot"></span><span>Fontenot Bayou Grillhouse</span></div>

  <span class="website">www.fontenotgrill.example</span>
</section>

<section class="card card--front" aria-label="Card front">
  <svg class="card__band" viewBox="0 0 680 388" aria-hidden="true">
    <defs>
      <linearGradient id="band-front" x1="0" y1="0" x2="1" y2="0">
        <stop offset="0" stop-color="#6cc04a"/>
        <stop offset=".3" stop-color="#d9b12a"/>
        <stop offset=".65" stop-color="#ee8a22"/>
        <stop offset="1" stop-color="#e0262b"/>
      </linearGradient>
    </defs>
    <path d="M680 332 H380 Q362 332 353 346 L342 366 Q336 374 324 374 H0 V388 H680 Z" fill="url(#band-front)"/>
  </svg>

  <div class="brand"><span class="brand__dot"></span><span>Fontenot Bayou Grillhouse</span></div>

  <div class="owner">
    <h1 class="owner__name">Darvel Pruitt</h1>
    <ul class="contact">
      <li class="contact__item">
        <svg class="contact__icon" viewBox="0 0 24 24" aria-label="Phone" role="img">
          <path fill="var(--green)" d="M6.6 10.8a15.1 15.1 0 0 0 6.6 6.6l2.2-2.2c.3-.3.7-.4 1-.2 1.1.4 2.3.6 3.6.6.6 0 1 .4 1 1V20c0 .6-.4 1-1 1A17 17 0 0 1 3 4c0-.6.4-1 1-1h3.5c.6 0 1 .4 1 1 0 1.3.2 2.5.6 3.6.1.3 0 .7-.2 1z"/>
        </svg>
        <span>(510) 493-2615</span>
      </li>
      <li class="contact__item">
        <svg class="contact__icon" viewBox="0 0 24 24" aria-label="Email" role="img">
          <path fill="var(--yellow)" d="M2 5h20v14H2z"/>
          <path fill="none" stroke="#0f0f0f" stroke-width="1.6" d="M2 5l10 8 10-8"/>
        </svg>
        <span>Dpruittkr4@mailvane.example</span>
      </li>
      <li class="contact__item">
        <svg class="contact__icon" viewBox="0 0 24 24" aria-label="Address" role="img">
          <path fill="var(--red)" d="M12 2a7 7 0 0 0-7 7c0 5.2 7 13 7 13s7-7.8 7-13a7 7 0 0 0-7-7zm0 9.5A2.5 2.5 0 1 1 12 6.5a2.5 2.5 0 0 1 0 5z"/>
        </svg>
        <span>327 Oakmere Street</span>
      </li>
    </ul>
  </div>

  <span class="website">www.fontenotgrill.example</span>
</section>

</body>
</html>
```